Bewerbungs-Template
Zielgruppe
Ich bin einen Einzelperson und möchte meine Bewerbungsunterlagen überarbeiten. Meine Zielgruppe ist ein potentieller Arbeitgeber welcher überzeugen möchte.
Aufgabenstellung
Das Design sollte professionell und übersichtlich aussehen und ein bisschen einzigartig sein. Es sollte nicht nur ein Deckblatt sein, wichtig ist für mich vor allem die CV-Gestaltung. Es muss kein Word-Format sein, kann mit den gängigen Office oder Photoprogrammen erstellt werden. In meinem Kopf schwirrt eine schlichte Idee mit einem Bordeaux-Roten Highlight herum, vlt. hat jemand eine Gute Idee :)
Ich bedanke mich bereits im Voraus für alle Ideen.

```html
<!DOCTYPE html>
<html lang="de">
<head>
<meta charset="utf-8">
<title>Lebenslauf Heike Brandt</title>
<link rel="stylesheet" href="https://fonts.googleapis.com/css2?family=Noto+Sans:wght@300;400&display=swap">
<style>
  :root {
    --bordeaux: #822436;
    --ink: #111111;
    --text: #222222;
    --paper: #ffffff;
  }
  * { margin: 0; padding: 0; box-sizing: border-box; }
  html, body { width: 849px; height: 1200px; overflow: hidden; background: var(--paper); }
  .cv {
    position: relative; width: 849px; height: 1200px;
    font-family: "Noto Sans", sans-serif; color: var(--text);
  }
  .band { position: absolute; left: 0; width: 849px; height: 16px; background: var(--bordeaux); }
  .band--top { top: 0; }
  .band--bottom { bottom: 0; }

  .title { position: absolute; left: 117px; top: 86px; font-weight: 300; line-height: 1.1; }
  .title__label { display: block; font-size: 30px; color: var(--bordeaux); letter-spacing: 0.02em; }
  .title__name { display: block; font-size: 31px; color: var(--ink); letter-spacing: 0.04em; margin-top: 1px; }

  .portrait { position: absolute; left: 610px; top: 56px; width: 175px; height: 175px; }

  .rule { position: absolute; left: 115px; top: 240px; width: 2px; height: 851px; background: var(--bordeaux); }

  .row { position: absolute; left: 162px; font-size: 17px; line-height: 21px; }
  .row__label { position: absolute; left: 0; white-space: nowrap; color: var(--bordeaux); letter-spacing: 0.02em; }
  .row__label--plain { color: var(--ink); }
  .row__value { position: absolute; left: 181px; white-space: nowrap; font-weight: 300; letter-spacing: 0.07em; color: var(--text); }

  .section-head { position: absolute; left: 162px; font-size: 23px; line-height: 28px; color: var(--ink); letter-spacing: 0.03em; font-weight: 400; }
</style>
</head>
<body>
<main class="cv">
  <div class="band band--top"></div>

  <h1 class="title">
    <span class="title__label">Lebenslauf</span>
    <span class="title__name">Heike Brandt</span>
  </h1>

  <svg class="portrait" viewBox="0 0 175 175" role="img" aria-label="Porträtfoto der Bewerberin">
    <defs>
      <radialGradient id="portrait-fill" cx="50%" cy="40%" r="60%">
        <stop offset="0%" stop-color="#e7c3a6"/>
        <stop offset="55%" stop-color="#c9d3e3"/>
        <stop offset="100%" stop-color="#eef1f5"/>
      </radialGradient>
    </defs>
    <circle cx="87.5" cy="87.5" r="86.5" fill="url(#portrait-fill)" stroke="var(--bordeaux)" stroke-width="1.6"/>
  </svg>

  <div class="rule"></div>

  <section class="personal">
    <div class="row" style="top:238px"><span class="row__label">Anschrift</span><span class="row__value">Lindenweg 7<br>54321 Beispielstadt</span></div>
    <div class="row" style="top:300px"><span class="row__label">Telefon</span><span class="row__value">0151 / 98765432</span></div>
    <div class="row" style="top:341px"><span class="row__label">E-Mail</span><span class="row__value">post@brandt-beispiel.de</span></div>
    <div class="row" style="top:382px"><span class="row__label">Geburt</span><span class="row__value">10.04.1985 | Beispielstadt</span></div>
    <div class="row" style="top:423px"><span class="row__label">Nationalität</span><span class="row__value">unbekannt</span></div>
    <div class="row" style="top:464px"><span class="row__label">Familienstand</span><span class="row__value">unbekannt</span></div>
  </section>

  <section class="education">
    <h2 class="section-head" style="top:547px">Ausbildung</h2>
    <div class="row" style="top:595px"><span class="row__label">1991/1995</span><span class="row__value">Grundschule Beispielstadt</span></div>
    <div class="row" style="top:636px"><span class="row__label">1995/2004</span><span class="row__value">Weiterführende Schule</span></div>
    <div class="row" style="top:677px"><span class="row__label">2004/2007</span><span class="row__value">abgeschlossene<br>Ausbildung / Studium</span></div>
  </section>

  <section class="experience">
    <h2 class="section-head" style="top:759px">Berufserfahrung</h2>
    <div class="row" style="top:807px"><span class="row__label">2007/2012</span><span class="row__value">Arbeitgeber I</span></div>
    <div class="row" style="top:848px"><span class="row__label">2012/2016</span><span class="row__value">Arbeitgeber II</span></div>
  </section>

  <section class="skills">
    <h2 class="section-head" style="top:930px">Kenntnisse</h2>
    <div class="row" style="top:978px"><span class="row__label row__label--plain">EDV</span><span class="row__value">Bürosoftware Text, Tabelle und Datenbank</span></div>
    <div class="row" style="top:1019px"><span class="row__label row__label--plain">Sprachen</span><span class="row__value">Deutsch, Englisch, Spanisch</span></div>
    <div class="row" style="top:1060px"><span class="row__label row__label--plain">Führerschein</span><span class="row__value">Klasse B</span></div>
  </section>

  <div class="band band--bottom"></div>
</main>
</body>
</html>
```